Design Artist Website for Data and Commerce

I am an artist and I need a website to be designed to share my portfolio with a large audience and sell my pieces. The Web site must be just like an art gallery white walls - a clean, simple place to display my artwork. The navigation and content should be straightforward in order to attract visitors and keep them on the site. A simple homepage for first-time visitors to understand who I am, my inspiration and my message, what my art looks like, what it's about, why it's worth seeing (and hopefully worth buying), and how to move around in order to get wherever they want to go. The website should also organize my art into groups and/or series of related works.

here is a link to an example of what am i looking for www.mirenholt.com. I absolutely LOVE the simplicity, elegance, and the page titles with the categories

Target Market(s)

•The Target Market / Audience you are trying to target

•Group age 30-60, yearly income 60k+
•People that are going through life changing events: marriage, newborn, divorce, separation, death, buyers & renters.

Number of Pages Required

5+ page

Font styles to use
Sans Serif

Colors
ffffff
f3f1f8

Requirements
Must have
• •Homepage links: view art, search, bookmark, share, purchase, browse, write reviews (reviews with curating rights)
• •The ability to request commission work
• •Purchase (message of payment CoinDrift, Orbo, PlenumCard)
• •A design that will display consistently on Internet Explorer, Google Chrome, Firefox and Safari
• • Meta descriptions
• • ability Reciprocal links
• • text on pages ( like a 2nd meta tags)
• • SEO
• •Mobile friendly, tablets, bramtab, smart phones and etc
• •The ability to upload my own work
• •The Ability to connect to social media: KV, Quillboard, Frameloop, Vantly, Nuvro
• • My name and contact info on every page
• • Ability to change design myself in future
• • 12-point font that contrasts with the background
• • consistent navigation for visitors to go any direction on my site ( back button doesn't count)
Nice to have
• I prefer minimalistic classic design to highlight the Art
• The ability to monitor the site by a dashboard that would include how many visits, how long a user in on the site, the pages that are visited most
• A theme that is modern that runs throughout the website that doesn't detract from the Art.
Should not have
• Anything or any type design that creates the users to experience long load time. The website will be heavy on images but it must remain easy and fast to access.

```html
<!DOCTYPE html>
<html lang="en">
<head>
<meta charset="utf-8">
<title>Mirela Castaine — Art</title>
<link rel="stylesheet" href="https://fonts.googleapis.com/css2?family=Gelasio:ital,wght@0,400;0,700;1,400;1,700&display=swap">
<style>
:root{
  --linen:#d8d1c2;
  --linen-dark:#cbc3b2;
  --floor:#f3f3f3;
  --white:#ffffff;
  --ink:#222222;
  --muted:#8a8a8a;
  --rule:#e2e2e2;
  --panel:#1a1a1a;
  --gold:#eba320;
  --button:#333333;
}
*{box-sizing:border-box;margin:0;padding:0}
html,body{width:1200px;height:2449px;overflow:hidden}
body{
  position:relative;
  font-family:"Gelasio",Georgia,serif;
  color:var(--ink);
  background:linear-gradient(to bottom,var(--linen) 0,var(--linen-dark) 2082px,var(--floor) 2082px);
}
.page{
  position:absolute;left:98px;top:44px;width:1003px;height:2218px;
  background:var(--white);
  padding:0 13px;
  box-shadow:0 4px 22px rgba(0,0,0,.28);
}
.site-header{height:144px;display:flex;align-items:center;justify-content:center;border-bottom:1px solid var(--rule);margin:0 -13px}
.brand{font-size:58px;font-weight:400;letter-spacing:1px;padding-top:6px}
.main-nav{height:72px;display:flex;justify-content:space-between;align-items:center;padding:0 16px}
.main-nav a{font-size:15px;text-transform:uppercase;color:var(--ink);text-decoration:none}
.hero{
  position:relative;height:556px;
  background:
    linear-gradient(to bottom,rgba(190,40,80,0) 40%,rgba(60,20,30,.35) 100%),
    linear-gradient(100deg,#a8203c 0%,#d9536e 25%,#f0c8a8 48%,#c94a5e 70%,#7a1e34 100%);
}
.hero-title{position:absolute;top:258px;width:100%;text-align:center;color:var(--white);font-size:39px;font-style:italic;font-weight:700;text-shadow:0 2px 6px rgba(0,0,0,.35)}
.slider-dots{position:absolute;top:510px;left:449px;display:flex;gap:9px}
.slider-dots span{width:14px;height:14px;border-radius:50%;background:var(--white)}
.slider-dots span.is-active{background:var(--gold)}
.artist-intro{height:387px;background:var(--panel);display:flex;padding:70px 0 0 20px}
.portrait-frame{width:359px;height:253px;border:6px solid var(--white);flex:none}
.portrait{width:100%;height:100%;background:linear-gradient(120deg,#4a3a34 0%,#c98f7a 35%,#e8a9c4 65%,#2c6fa8 100%)}
.intro-text{margin-left:34px;width:555px;color:var(--white)}
.intro-name{color:var(--gold);font-size:30px;font-style:italic;font-weight:700;line-height:1;margin-top:-2px}
.intro-quote{font-size:18px;margin-top:14px}
.intro-motto{font-size:18px;margin-top:10px}
.intro-body{font-size:14px;line-height:26px;margin-top:26px}
.products-heading{height:114px;border-bottom:1px solid var(--rule);text-align:center;font-size:31px;font-weight:400;padding-top:55px;line-height:40px}
.product-grid{display:grid;grid-template-columns:309px 307px 309px;column-gap:26px;row-gap:48px;margin-top:21px}
.product{height:368px}
.product-art{height:245px}
.art-1{background:linear-gradient(160deg,#2fc3a0 0%,#1b8f86 35%,#6a4fa0 65%,#a66a80 100%)}
.art-2{background:linear-gradient(to bottom,#c79ad8 0%,#e6b9d6 30%,#2a3cc0 55%,#c21d3c 80%,#3a1a1a 100%)}
.art-3{background:linear-gradient(135deg,#8c7fd9 0%,#c84468 40%,#b9b2e8 70%,#6f66c4 100%)}
.art-4{background:linear-gradient(130deg,#b07a62 0%,#7a3b8c 45%,#3b1d5a 75%,#a77a6a 100%)}
.art-5{background:linear-gradient(to bottom,#c9a8b8 0%,#7a4a8a 40%,#5a2c6a 70%,#6c7bc0 100%)}
.art-6{background:linear-gradient(120deg,#3e8f3a 0%,#b9d48a 30%,#c8486a 55%,#f0c4cc 75%,#2f7a30 100%)}
.product-title{font-size:21px;font-weight:400;margin-top:8px;line-height:26px}
.product-desc{font-size:11.5px;color:var(--muted);line-height:21px;margin-top:3px;width:300px}
.btn-view{display:inline-flex;align-items:center;justify-content:center;width:100px;height:30px;margin-top:17px;background:var(--button);color:var(--white);font-size:12px;font-style:italic;font-weight:700;text-decoration:none}
.more-wrap{text-align:center;margin-top:47px}
.btn-more{display:inline-flex;align-items:center;justify-content:center;width:265px;height:52px;background:var(--button);color:var(--white);font-size:21px;text-decoration:none}
.site-footer{position:absolute;left:0;top:2296px;width:1200px;text-align:center;font-size:12px}
.footer-bar{display:flex;justify-content:center;align-items:center;gap:60px;height:42px}
.footer-group{display:flex;align-items:center;gap:12px}
.social{display:flex;gap:12px}
.social span{display:flex;align-items:center;gap:4px;font-size:12px}
.social span::before{content:"";width:10px;height:10px;border-radius:50%;background:var(--ink)}
.pay{display:inline-flex;align-items:center;justify-content:center;height:28px;padding:0 10px;background:var(--white);font-size:12px;color:var(--ink)}
.footer-nav{display:flex;justify-content:center;margin-top:33px}
.footer-nav a{color:var(--ink);text-decoration:none;padding:0 16px;border-left:1px solid var(--ink);line-height:13px}
.footer-nav a:first-child{border-left:none}
.copyright{margin-top:22px}
</style>
</head>
<body>
<div class="page">
  <header class="site-header"><div class="brand">Mirela Castaine</div></header>
  <nav class="main-nav">
    <a href="#">Home</a><a href="#">View Art</a><a href="#">Search</a><a href="#">Bookmark</a><a href="#">Share</a><a href="#">Purchase</a><a href="#">Browse</a><a href="#">Write Reviews</a><a href="#">Contact Us</a>
  </nav>
  <section class="hero" role="img" aria-label="Featured painting: abstract city skyline in crimson, pink and cream brushstrokes">
    <h1 class="hero-title">Mirela Castaine</h1>
    <div class="slider-dots"><span class="is-active"></span><span></span><span></span><span></span></div>
  </section>
  <section class="artist-intro">
    <div class="portrait-frame"><div class="portrait" role="img" aria-label="Portrait of the artist holding a brush beside a pink blossom painting"></div></div>
    <div class="intro-text">
      <h2 class="intro-name">Mirela Castaine</h2>
      <p class="intro-quote">"From the North with Warmth"</p>
      <p class="intro-motto">Art heals the soul.</p>
      <p class="intro-body">Mirela embraces all of life; the light and the dark, the calm and the storm. Passion fills her heart as she lets her entire body flow with every stroke of the brush. What results are feelings captured on canvas. Mirela's art is heavily influenced by the raw and natural aspects of the world. She seeks to connect with others through her art. This stems from an understanding of the truth behind human emotion.</p>
    </div>
  </section>
  <section class="products">
    <h2 class="products-heading">OUR PRODUCTS</h2>
    <div class="product-grid">
      <article class="product"><div class="product-art art-1" role="img" aria-label="Painting: turquoise arches over a violet abstract city"></div><h3 class="product-title">Mirela Castaine Art</h3><p class="product-desc">Neque porro quisquam est qui dolorem ipsum quia dolor sit amet, consectetur, adipisci velit..."</p><a class="btn-view" href="#">View Art</a></article>
      <article class="product"><div class="product-art art-2" role="img" aria-label="Painting: blue blossoms on a branch above a red field"></div><h3 class="product-title">Mirela Castaine Art</h3><p class="product-desc">Neque porro quisquam est qui dolorem ipsum quia dolor sit amet, consectetur, adipisci velit..."</p><a class="btn-view" href="#">View Art</a></article>
      <article class="product"><div class="product-art art-3" role="img" aria-label="Painting: red leaves on birch trees against lavender"></div><h3 class="product-title">Mirela Castaine Art</h3><p class="product-desc">Neque porro quisquam est qui dolorem ipsum quia dolor sit amet, consectetur, adipisci velit..."</p><a class="btn-view" href="#">View Art</a></article>
      <article class="product"><div class="product-art art-4" role="img" aria-label="Painting: purple dress with dripping paint"></div><h3 class="product-title">Mirela Castaine Art</h3><p class="product-desc">Neque porro quisquam est qui dolorem ipsum quia dolor sit amet, consectetur, adipisci velit..."</p><a class="btn-view" href="#">View Art</a></article>
      <article class="product"><div class="product-art art-5" role="img" aria-label="Painting: violet corset bodice on blue ground"></div><h3 class="product-title">Mirela Castaine Art</h3><p class="product-desc">Neque porro quisquam est qui dolorem ipsum quia dolor sit amet, consectetur, adipisci velit..."</p><a class="btn-view" href="#">View Art</a></article>
      <article class="product"><div class="product-art art-6" role="img" aria-label="Painting: swirling pink figure on green"></div><h3 class="product-title">Mirela Castaine Art</h3><p class="product-desc">Neque porro quisquam est qui dolorem ipsum quia dolor sit amet, consectetur, adipisci velit..."</p><a class="btn-view" href="#">View Art</a></article>
    </div>
    <div class="more-wrap"><a class="btn-more" href="#">View More Art Works</a></div>
  </section>
</div>
<footer class="site-footer">
  <div class="footer-bar">
    <div class="footer-group"><span>Connect With Us</span>
      <div class="social"><span>Vantly</span><span>KV</span><span>Nuvro</span><span>Quillboard</span><span>Frameloop</span></div>
    </div>
    <div class="footer-group"><span>Payments Via</span>
      <span class="pay">CoinDrift</span><span class="pay">Orbo</span><span class="pay">PlenumCard</span>
    </div>
  </div>
  <nav class="footer-nav">
    <a href="#">Home</a><a href="#">View Art</a><a href="#">Search</a><a href="#">Bookmark</a><a href="#">Share</a><a href="#">Purchase</a><a href="#">Browse</a><a href="#">Write Reviews</a><a href="#">Contact Us</a>
  </nav>
  <p class="copyright">© 2015 Company Name,All Rights Reserved</p>
</footer>
</body>
</html>
```